Seeking Talented PSD Designer for Real Estate Finance Web Site

Hello ...
Need a minimalist design for a high - end finance web site that conveys prestige / sophistication / class ... Below are comps for this project ...
http://www.tawnyridgefunding.com/
http://glenmoorfunds.com/
http://www.cedarloftfp.com/
http://halvornfunds.com/
Look forward too receiving proposals for this project ....
Target Market(s)
Commerciale entities seeking more than $500.0 k in interim capital ... These could include apartment owners / construction managers / restaurant owners / hotels / golf courses ...
Industry/Entity Type
Real Estate
Number of Pages Required
1 page
Requirements
Must have
- Super high quality graphic design ... Has to be marketable and convert customers to contact us ...
- Please refer to logo concept four ....
Should not have
- clunky / poor fonts /

```html
<!DOCTYPE html>
<html lang="en">
<head>
<meta charset="utf-8">
<title>Halden Capital – Real Estate Finance Services</title>
<link rel="stylesheet" href="https://fonts.googleapis.com/css2?family=Catamaran:wght@600;700&family=Raleway:wght@400;500;600&family=Open+Sans:wght@400;600&display=swap">
<style>
  :root{
    --blue-deep:#1a4fa6;
    --blue-hero:#2a67c4;
    --blue-band:#2f72b8;
    --blue-title:#2b63b5;
    --navy-text:#2d4670;
    --ink:#2b2b2b;
    --body:#666a70;
    --grey-bg:#d9dbdf;
    --white:#ffffff;
    --line:#dfe3e8;
  }
  *{box-sizing:border-box;margin:0;padding:0}
  html,body{width:825px;height:1200px;overflow:hidden;background:var(--white)}
  body{position:relative;font-family:"Open Sans",sans-serif;color:var(--body)}

  /* hero */
  .hero{position:absolute;left:0;top:0;width:825px;height:388px;
    background:linear-gradient(180deg,#1d55b0 0%,#3a78d0 45%,#5a8fd6 80%,#2f62b0 100%);}
  .hero-photo{position:absolute;inset:0;
    background:
      linear-gradient(90deg,rgba(20,60,140,.55) 0%,rgba(20,60,140,0) 25%,rgba(20,60,140,0) 75%,rgba(20,60,140,.55) 100%),
      radial-gradient(ellipse at 50% 55%,rgba(160,200,245,.45),rgba(160,200,245,0) 60%);}
  .brand{position:absolute;left:106px;top:22px;display:flex;align-items:center;gap:8px}
  .brand-dot{width:46px;height:46px;border-radius:50%;background:var(--white);flex:none}
  .brand-name{font-family:"Raleway",sans-serif;font-weight:400;color:var(--white);font-size:14px;letter-spacing:2px;white-space:nowrap}
  .main-nav{position:absolute;top:40px;left:343px;font-family:"Raleway",sans-serif;font-weight:500;font-size:10.5px;color:var(--white)}
  .main-nav a{color:inherit;text-decoration:none;position:absolute;white-space:nowrap}
  .main-nav a.active::after{content:"";position:absolute;left:0;right:0;top:19px;height:2px;background:var(--white)}
  .hero-copy{position:absolute;left:0;width:825px;top:146px;text-align:center;color:var(--white);font-family:"Catamaran",sans-serif}
  .hero-title{font-weight:700;font-size:35px;line-height:40px;letter-spacing:.3px}
  .hero-sub{font-weight:700;font-size:24px;line-height:26px;margin-top:-1px}
  .btn-ghost{display:inline-block;border:1.5px solid var(--white);color:var(--white);font-family:"Raleway",sans-serif;text-decoration:none}
  .hero-btn{position:absolute;left:364px;top:228px;width:95px;height:30px;line-height:27px;text-align:center;font-size:10.5px;font-weight:500}
  .arrow{position:absolute;top:178px}

  /* welcome */
  .welcome{position:absolute;left:0;top:388px;width:825px;height:210px;background:var(--white)}
  .welcome h1{position:absolute;left:110px;top:42px;font-family:"Raleway",sans-serif;font-weight:400;font-size:20.5px;color:var(--ink);white-space:nowrap}
  .welcome .lead{position:absolute;left:110px;top:76px;width:470px;font-size:8.6px;line-height:14.5px;color:#5d6066}
  .welcome .more{position:absolute;left:110px;top:115px;width:470px;font-size:7.3px;line-height:14.2px;color:#6a6d72}
  .welcome-seal{position:absolute;left:598px;top:43px;width:111px;height:111px;border-radius:50%;background:#d8dde7}

  /* services */
  .services{position:absolute;left:0;top:598px;width:825px;height:237px;
    background:linear-gradient(135deg,#3a7cc3 0%,#2f71b7 40%,#2a69b0 70%,#3479c0 100%)}
  .service{position:absolute;top:24px;width:200px;text-align:center;color:var(--white)}
  .service .icon{display:block;margin:0 auto}
  .service h2{font-family:"Raleway",sans-serif;font-weight:500;font-size:14.5px;margin-top:8px;letter-spacing:.2px}
  .service p{font-size:7.6px;line-height:11.5px;color:#dce8f6;margin-top:5px}
  .service .btn-ghost{margin-top:11px;width:67px;height:21px;line-height:18px;font-size:7px;font-weight:600;border-width:1.3px}

  /* projects */
  .projects{position:absolute;left:0;top:835px;width:825px;height:276px;
    background:linear-gradient(180deg,#d4d6da 0%,#e2e3e6 50%,#d6d8dc 100%)}
  .divider-dot{position:absolute;left:396px;top:819px;width:32px;height:32px;border-radius:50%;background:var(--white);z-index:2}
  .divider-dot::after{content:"";position:absolute;left:5px;top:5px;width:22px;height:22px;border-radius:50%;background:#3d5f92}
  .projects h2{position:absolute;left:0;width:825px;top:34px;text-align:center;font-family:"Raleway",sans-serif;font-weight:400;font-size:18px;color:var(--navy-text)}
  .card{position:absolute;top:76px;width:194px;height:156px;background:var(--white)}
  .card .photo{height:107px}
  .card h3{text-align:center;font-family:"Raleway",sans-serif;font-weight:500;font-size:11px;color:var(--blue-title);margin-top:8px}
  .card p{text-align:center;font-size:7.5px;color:#6a6d72;margin-top:3px}

  /* footer */
  .site-footer{position:absolute;left:0;top:1111px;width:825px;height:89px;background:var(--white)}
  .foot-nav{position:absolute;top:29px;left:109px;font-family:"Raleway",sans-serif;font-weight:500;font-size:10px;color:var(--ink)}
  .foot-nav a{position:absolute;color:inherit;text-decoration:none;white-space:nowrap}
  .copyright{position:absolute;left:109px;top:52px;font-size:7.2px;color:#6a6d72;white-space:nowrap}
  .social{position:absolute;left:630px;top:27px;display:flex;gap:2px}
  .social span{width:20px;height:20px;border-radius:50%;border:1.2px solid #333}
</style>
</head>
<body>

<header class="hero">
  <div class="hero-photo" role="img" aria-label="Blue-tinted upward view of city skyscrapers"></div>

  <div class="brand">
    <span class="brand-dot"></span>
    <span class="brand-name">HALDEN CAPITAL</span>
  </div>

  <nav class="main-nav">
    <a class="active" style="left:0">HOME</a>
    <a style="left:54px">ABOUT US</a>
    <a style="left:128px">SERVICES</a>
    <a style="left:200px">PROJECTS</a>
    <a style="left:274px">TEAM</a>
    <a style="left:326px">CONTACT</a>
  </nav>

  <svg class="arrow" style="left:86px" width="14" height="24" viewBox="0 0 14 24"><path d="M12 2 L3 12 L12 22" fill="none" stroke="#fff" stroke-width="2.5"/></svg>
  <svg class="arrow" style="left:724px" width="14" height="24" viewBox="0 0 14 24"><path d="M2 2 L11 12 L2 22" fill="none" stroke="#fff" stroke-width="2.5"/></svg>

  <div class="hero-copy">
    <div class="hero-title">REAL ESTATE FINANCE SERVICES</div>
    <div class="hero-sub">MAURIS VEL LACUS VITAE FELIS</div>
  </div>
  <a class="btn-ghost hero-btn">LEARN MORE</a>
</header>

<section class="welcome">
  <h1>WELCOME TO HALDEN CAPITAL</h1>
  <p class="lead">Mauris vel lacus vitae felis vestibulum volutpat imperdiet ac nisl Cum sociis natoque penatibus et magnis dis parturient montes nascetur ridiculus mus In iaculis facilisis massa</p>
  <p class="more">Vivamus porttitor purus nisi eleifend libero a tempus libero lectus feugiat felis Morbi diam mauris viverra in gravida eu mattis in ante Morbi eget arcu Morbi porta libero id ullamcorper nonummy nibh ligula pulvinar metus eget consectetuer augue nisi quis lacus Ut ac mi quis lacus mollis aliquam Curabitur iaculis tempus eros Curabitur vel mi sit amet magna males</p>
  <div class="welcome-seal"></div>
</section>

<section class="services">
  <div class="service" style="left:107px">
    <svg class="icon" width="80" height="86" viewBox="0 0 80 86">
      <circle cx="40" cy="40" r="38" fill="none" stroke="#fff" stroke-width="1.6"/>
      <path d="M33 77 L40 84 L47 77 Z" fill="#fff"/>
      <path d="M24 58 V25 Q30 20 40 21 V58 Z M40 58 V35 H56 V58 Z" fill="#fff"/>
      <g fill="#2f71b7"><rect x="28" y="30" width="8" height="2"/><rect x="28" y="36" width="8" height="2"/><rect x="28" y="42" width="8" height="2"/><rect x="28" y="48" width="8" height="2"/><rect x="45" y="44" width="6" height="14"/></g>
    </svg>
    <h2>COMMERCIAL</h2>
    <p>Lorem ipsum dolor sit amet consectetuer<br>adipiscing elit Nam cursus Morbi ut mi</p>
    <a class="btn-ghost">LEARN MORE</a>
  </div>
  <div class="service" style="left:313px">
    <svg class="icon" width="80" height="86" viewBox="0 0 80 86">
      <circle cx="40" cy="40" r="38" fill="none" stroke="#fff" stroke-width="1.6"/>
      <path d="M33 77 L40 84 L47 77 Z" fill="#fff"/>
      <path d="M20 40 L40 22 L60 40" fill="none" stroke="#fff" stroke-width="3"/>
      <rect x="26" y="20" width="5" height="10" fill="#fff"/>
      <rect x="26" y="40" width="28" height="18" fill="none" stroke="#fff" stroke-width="3"/>
      <rect x="31" y="45" width="7" height="13" fill="#fff"/><rect x="43" y="44" width="7" height="6" fill="#fff"/>
    </svg>
    <h2>RESIDENTIAL</h2>
    <p>Lorem ipsum dolor sit amet consectetuer<br>adipiscing elit Nam cursus Morbi ut mi</p>
    <a class="btn-ghost">LEARN MORE</a>
  </div>
  <div class="service" style="left:510px">
    <svg class="icon" width="80" height="86" viewBox="0 0 80 86" role="img" aria-label="Handshake icon">
      <circle cx="40" cy="40" r="38" fill="none" stroke="#fff" stroke-width="1.6"/>
      <path d="M33 77 L40 84 L47 77 Z" fill="#fff"/>
      <path d="M18 34 L26 28 L40 40 L54 28 L62 34 L48 52 H32 Z" fill="none" stroke="#fff" stroke-width="2.4" stroke-linejoin="round"/>
    </svg>
    <h2>BUSINESS</h2>
    <p>Lorem ipsum dolor sit amet consectetuer<br>adipiscing elit Nam cursus Morbi ut</p>
    <a class="btn-ghost">LEARN MORE</a>
  </div>
</section>

<div class="divider-dot"></div>

<section class="projects" role="region" aria-label="Recent projects over a faded grey city skyline">
  <h2>RECENT PROJECTS</h2>
  <article class="card" style="left:106px">
    <div class="photo" role="img" aria-label="Glass office building beside green trees" style="background:linear-gradient(180deg,#7fa9d8 0%,#5e7a8e 55%,#5b7a45 100%)"></div>
    <h3>PROPERTY TITTLE</h3>
    <p>Curabitur vel mi sit amet magna males</p>
  </article>
  <article class="card" style="left:316px">
    <div class="photo" role="img" aria-label="Two-storey family house at dusk with lit windows" style="background:linear-gradient(180deg,#8ea9c9 0%,#a59a8a 55%,#4f6b3a 100%)"></div>
    <h3>PROPERTY TITTLE</h3>
    <p>Curabitur vel mi sit amet magna males</p>
  </article>
  <article class="card" style="left:524px">
    <div class="photo" role="img" aria-label="Backyard patio with wooden deck and lit house" style="background:linear-gradient(180deg,#3f4a3a 0%,#8a7a60 50%,#6b4a30 100%)"></div>
    <h3>PROPERTY TITTLE</h3>
    <p>Curabitur vel mi sit amet magna males</p>
  </article>
</section>

<footer class="site-footer">
  <nav class="foot-nav">
    <a style="left:0">HOME</a>
    <a style="left:54px">ABOUT US</a>
    <a style="left:128px">SERVICES</a>
    <a style="left:200px">PROJECTS</a>
    <a style="left:273px">TEAM</a>
    <a style="left:325px">CONTACT</a>
  </nav>
  <p class="copyright">© 2016 Company Name &nbsp;All right reserved &nbsp;Term of Use</p>
  <div class="social"><span></span><span></span><span></span><span></span></div>
</footer>

</body>
</html>
```